Create business card using existing logo idea and create other designs for me to choose from

am looking for a creative graphic designer to design me business cards for my business would like the grey in the logo to be black aswell as adding some sort of dynamic to give it more of an edge, will provide details while will need to go on the card aswell, i would like the designer to also come up with a few other logos and create templates with details so i can decide which one i would like other than the ideas ive provided myself

double sided with the logo and company name on one side and details and smaller avatar of logo on the other

```html
<!DOCTYPE html>
<html lang="en">
<head>
<meta charset="UTF-8">
<title>Brightline Painting &amp; Decorating – Business Card</title>
<link rel="stylesheet" href="https://fonts.googleapis.com/css2?family=Open+Sans:wght@400;600;700&display=swap">
<style>
  :root {
    --backdrop: #2b2e33;
    --card: #ffffff;
    --brand-red: #e3161e;
    --ink: #1a1a1a;
    --ink-soft: #555a60;
    --photo-light: #c9c4ba;
    --photo-mid: #8d8f8a;
    --photo-dark: #4d5a45;
  }
  html, body {
    margin: 0;
    padding: 0;
    width: 1200px;
    height: 900px;
    overflow: hidden;
    background: var(--backdrop);
    font-family: "Open Sans", Arial, sans-serif;
  }
  .canvas {
    width: 1200px;
    height: 900px;
    display: flex;
    flex-direction: column;
    align-items: center;
    justify-content: center;
    gap: 60px;
  }
  .card {
    display: block;
    width: 600px;
    height: 343px;
    box-shadow: 0 10px 30px rgba(0,0,0,0.45);
  }
  .card-bg { fill: var(--card); }
  .accent { fill: var(--brand-red); }
  .accent-line { stroke: var(--brand-red); fill: none; }
  .brand-name {
    font-family: "Open Sans", Arial, sans-serif;
    font-weight: 700;
    font-size: 30px;
    fill: var(--ink);
  }
  .brand-dot { fill: var(--brand-red); }
  .call-line {
    font-size: 30px;
    font-weight: 400;
    fill: var(--ink-soft);
  }
  .call-line .call-word { fill: var(--brand-red); }
  .role {
    font-size: 19px;
    fill: var(--ink-soft);
  }
  .contact {
    font-size: 15px;
    fill: var(--ink);
  }
  .reg {
    font-size: 12.5px;
    fill: var(--ink-soft);
  }
  .icon-bg { fill: var(--ink); }
  .icon-fg { fill: #ffffff; stroke: none; }
  .icon-stroke { stroke: #ffffff; fill: none; stroke-width: 1.3; }
</style>
</head>
<body>
<main class="canvas">

  <!-- Front: company name -->
  <svg class="card card-front" viewBox="0 0 600 343" xmlns="http://www.w3.org/2000/svg">
    <defs>
      <linearGradient id="houseToneFront" x1="0" y1="0" x2="1" y2="1">
        <stop offset="0" stop-color="var(--photo-mid)"/>
        <stop offset="0.55" stop-color="var(--photo-light)"/>
        <stop offset="1" stop-color="var(--photo-dark)"/>
      </linearGradient>
    </defs>
    <rect class="card-bg" width="600" height="343"/>
    <polygon role="img" aria-label="Photo of a freshly painted house exterior" fill="url(#houseToneFront)" points="0,0 170,0 60,343 0,343"/>
    <line class="accent-line" x1="172" y1="-2" x2="62" y2="345" stroke-width="7"/>
    <polygon class="accent" points="170,0 260,0 255,6 168,6"/>
    <rect class="accent" x="588" y="250" width="12" height="40"/>
    <rect class="accent" x="588" y="298" width="12" height="26"/>
    <g class="brand" transform="translate(372 185)">
      <circle class="brand-dot" cx="-175" cy="-10" r="10"/>
      <text class="brand-name" x="-155" y="0">Brightline Painting</text>
      <text class="brand-name" x="-155" y="36">&amp; Decorating</text>
    </g>
  </svg>

  <!-- Back: contact details -->
  <svg class="card card-back" viewBox="0 0 600 343" xmlns="http://www.w3.org/2000/svg">
    <defs>
      <linearGradient id="houseToneBack" x1="0" y1="0" x2="1" y2="1">
        <stop offset="0" stop-color="var(--photo-mid)"/>
        <stop offset="0.5" stop-color="var(--photo-light)"/>
        <stop offset="1" stop-color="var(--photo-dark)"/>
      </linearGradient>
    </defs>
    <rect class="card-bg" width="600" height="343"/>

    <!-- red chevron frame -->
    <polygon class="accent" points="0,0 95,0 95,343 0,343"/>
    <polygon class="card-bg" points="14,14 80,14 80,60 42,90 42,253 80,283 80,329 14,329"/>
    <polygon class="accent" points="14,14 28,14 28,329 14,329"/>

    <!-- photo -->
    <polygon role="img" aria-label="Photo of a painted two-storey house with garage and hedge" fill="url(#houseToneBack)" points="410,0 600,0 600,343 500,343"/>
    <line class="accent-line" x1="408" y1="-2" x2="498" y2="345" stroke-width="7"/>

    <g class="details" transform="translate(115 0)">
      <text class="call-line" x="0" y="62"><tspan class="call-word">CALL</tspan> SAM ON</text>
      <text class="role" x="0" y="92">Owner</text>

      <g transform="translate(0 118)">
        <circle class="icon-bg" cx="8" cy="-5" r="8"/>
        <rect class="icon-stroke" x="3.5" y="-8.5" width="9" height="7"/>
        <polyline class="icon-stroke" points="3.5,-8.5 8,-4.5 12.5,-8.5"/>
        <text class="contact" x="24" y="0">hello@brightlinepaint.com</text>
      </g>
      <g transform="translate(0 146)">
        <circle class="icon-bg" cx="8" cy="-5" r="8"/>
        <path class="icon-fg" d="M4.5,-9.5 l2,-0.5 l1.2,2.6 l-1.2,1 q1,2.2 3,3 l1,-1.2 l2.6,1.2 l-0.5,2 q-4,0.4 -6.6,-2.4 q-2.2,-2.6 -1.5,-5.7z"/>
        <text class="contact" x="24" y="0">0400 555 018</text>
      </g>

      <text class="reg" x="0" y="182">ABN: 12 345 678 901</text>
      <text class="reg" x="0" y="200">LIC NO. 100234C</text>
    </g>
  </svg>

</main>
</body>
</html>
```